Relocation/furniture installation company needs new business cards

we are a relocation and furniture installation company mainly dealing with corporate clients and we are looking for new business card ideas. Cards should incorporate our logo and list our website, phone number and services. The company is only 2 years old but with more staff joining we are in the need for more business cards, so something with an awesome design that is eye catching would go a long way to insure we get our name out there and look good to potential new clients.

Target Market(s)

Corporate

Industry/Entity Type

Trade

Contact Information for Business Card

www.merovanta.co.nz
0508 7 kelpor

furniture installation
business relocations
joinery installation
commercial property maintenance

Colors
0592cd
34a7d8
85cae6
85acd3
0356a4
cfdfed
cee9f5
757575
474747

Requirements
Must have
• Business relocations and furniture installation specialists
Nice to have
• something that incorporates our logo.

```html
<!DOCTYPE html>
<html lang="en">
<head>
<meta charset="utf-8">
<title>Merovanta business cards</title>
<link href="https://fonts.googleapis.com/css2?family=Open+Sans:wght@400;600;700&display=swap" rel="stylesheet">
<style>
  :root {
    --blue-deep: #0356a4;
    --blue-main: #0592cd;
    --blue-bright: #34a7d8;
    --blue-soft: #85cae6;
    --blue-mist: #cfdfed;
    --navy: #1f2f8f;
    --paper: #f4f6f8;
    --paper-shade: #dde3ea;
    --grey-mid: #757575;
    --grey-dark: #474747;
    --backdrop: #e9e9e9;
  }
  * { box-sizing: border-box; margin: 0; padding: 0; }
  html, body { width: 1200px; height: 952px; overflow: hidden; }
  body {
    background: var(--backdrop);
    font-family: "Open Sans", Arial, sans-serif;
    position: relative;
  }
  .card {
    position: absolute;
    width: 640px;
    height: 366px;
    overflow: hidden;
    background: radial-gradient(ellipse at 45% 40%, #ffffff 0%, var(--paper) 45%, var(--paper-shade) 100%);
    box-shadow: 0 10px 30px rgba(0,0,0,.18);
  }
  .card-front { left: 60px; top: 80px; }
  .card-back { left: 500px; top: 500px; }
  .card-art { position: absolute; inset: 0; width: 100%; height: 100%; }

  .wordmark {
    color: var(--navy);
    font-weight: 700;
    letter-spacing: 6px;
    text-transform: uppercase;
    line-height: 1;
  }

  /* front */
  .front-content {
    position: absolute;
    left: 0; right: 0; top: 92px;
    text-align: center;
  }
  .front-content .wordmark { font-size: 50px; }
  .service-line {
    margin-top: 18px;
    font-size: 15px;
    font-weight: 600;
    color: var(--navy);
    display: flex;
    justify-content: center;
    gap: 18px;
  }
  .service-line + .service-line { margin-top: 6px; }
  .service-line span::before {
    content: "";
    display: inline-block;
    width: 6px; height: 6px;
    border-radius: 50%;
    background: var(--blue-bright);
    margin-right: 5px;
    vertical-align: middle;
  }
  .web-pill {
    display: inline-block;
    margin-top: 26px;
    padding: 6px 30px;
    border: 2px solid var(--blue-main);
    border-radius: 14px;
    color: var(--navy);
    font-weight: 700;
    font-size: 15px;
  }

  /* back */
  .service-list {
    position: absolute;
    right: 26px; top: 60px;
    width: 226px;
    list-style: none;
    color: #ffffff;
  }
  .service-list li {
    position: relative;
    padding: 4px 0 6px 16px;
    font-size: 17px;
    font-weight: 600;
    line-height: 1.2;
    border-bottom: 1.5px solid rgba(255,255,255,.85);
    margin-bottom: 8px;
  }
  .service-list li::before {
    content: "";
    position: absolute;
    left: 2px; top: 12px; bottom: -2px;
    width: 1.5px;
    background: #ffffff;
  }
  .service-list li::after {
    content: "";
    position: absolute;
    left: -1px; top: 9px;
    width: 7px; height: 7px;
    border-radius: 50%;
    background: #ffffff;
  }
  .back-contact {
    position: absolute;
    left: 30px; bottom: 40px;
    display: flex;
    align-items: center;
    gap: 18px;
  }
  .back-contact .wordmark { font-size: 30px; letter-spacing: 4px; }
  .contact-divider { width: 1.5px; height: 50px; background: var(--grey-dark); }
  .contact-call { color: var(--navy); font-weight: 700; font-size: 17px; }
  .contact-web { color: var(--navy); font-weight: 600; font-size: 12px; margin-top: 3px; }
</style>
</head>
<body>

<section class="card card-front" aria-label="Card front">
  <svg class="card-art" viewBox="0 0 640 366" preserveAspectRatio="none" aria-hidden="true">
    <defs>
      <linearGradient id="frontBlue" x1="0" y1="0" x2="1" y2="1">
        <stop offset="0" stop-color="var(--blue-main)"/>
        <stop offset="0.55" stop-color="var(--blue-deep)"/>
        <stop offset="1" stop-color="#023e7d"/>
      </linearGradient>
    </defs>
    <path d="M0 0 H40 L40 60 L80 100 V280 L40 320 V366 H0 Z" fill="url(#frontBlue)"/>
    <path d="M640 0 H600 L600 50 L560 90 V270 L600 310 V366 H640 Z" fill="url(#frontBlue)"/>
  </svg>
  <div class="front-content">
    <div class="wordmark">Merovanta</div>
    <div class="service-line">
      <span>Furniture installation</span>
      <span>Business relocations</span>
      <span>Joinery installation</span>
    </div>
    <div class="service-line">
      <span>commercial property maintenance</span>
    </div>
    <div class="web-pill">www.merovanta.co.nz</div>
  </div>
</section>

<section class="card card-back" aria-label="Card back">
  <svg class="card-art" viewBox="0 0 640 366" preserveAspectRatio="none" aria-hidden="true">
    <defs>
      <linearGradient id="backBlue" x1="0" y1="0" x2="1" y2="1">
        <stop offset="0" stop-color="var(--blue-deep)"/>
        <stop offset="0.5" stop-color="var(--blue-main)"/>
        <stop offset="1" stop-color="#023e7d"/>
      </linearGradient>
    </defs>
    <path d="M400 0 H640 V366 H440 V300 L380 250 V90 L400 70 Z" fill="url(#backBlue)"/>
  </svg>
  <ul class="service-list">
    <li>Furniture installation</li>
    <li>Business relocations</li>
    <li>Joinery installation</li>
    <li>Commercial property maintenance</li>
  </ul>
  <div class="back-contact">
    <div class="wordmark">Merovanta</div>
    <div class="contact-divider"></div>
    <div>
      <div class="contact-call">CALL : 0508 7 kelpor</div>
      <div class="contact-web">www.merovanta.co.nz</div>
    </div>
  </div>
</section>

</body>
</html>
```